Brookfell Self Storage - Business Sign

The sign we are needing designed is our main road sign for our self-storage business. The dimensions of the sign are 57 inches tall x 96 inches wide. We require that our attached logo be on the sign as well as our phone number: 478-216-4387 and website www.BrookfellStorage.net. Optional information that can be added but not required is our address: 418 Marlow Tenney Pkwy, Centerville, GA 31047.

Industry/Entity Type

Self Storage

Font styles to use
Sans Serif

```html
<!DOCTYPE html>
<html lang="en">
<head>
<meta charset="utf-8">
<title>Brookfell Self Storage – Road Sign</title>
<link rel="stylesheet" href="https://fonts.googleapis.com/css2?family=Barlow:wght@500;700;800&display=swap">
<style>
  :root {
    --ink: #3a3a3c;
    --brand-blue: #1f5bb5;
    --door-blue: #2452b0;
    --sky: #9cc2e8;
    --concrete: #d9d9d6;
    --slate: #3b3b3d;
    --paper: #ffffff;
  }
  * { margin: 0; padding: 0; box-sizing: border-box; }
  html, body { width: 1200px; height: 720px; overflow: hidden; background: var(--paper); }
  .sign {
    position: relative; width: 1200px; height: 720px; overflow: hidden;
    background: var(--paper); font-family: "Barlow", Arial, sans-serif; color: var(--ink);
  }
  .facility-photo {
    position: absolute; left: 520px; top: 150px; width: 680px; height: 570px;
    background:
      linear-gradient(180deg, var(--sky) 0%, #c9dcef 25%, var(--concrete) 38%, #c3c6cc 48%, var(--door-blue) 49%, #1d4596 100%);
  }
  .facility-photo::after {
    content: ""; position: absolute; inset: 0;
    background: linear-gradient(90deg, var(--paper) 0%, rgba(255,255,255,0.6) 20%, rgba(255,255,255,0) 45%);
  }
  .headline {
    position: absolute; left: 78px; top: 50px;
    font-weight: 800; font-size: 62px; line-height: 0.98; letter-spacing: 1px;
    text-transform: uppercase; color: var(--ink);
  }
  .brand {
    position: absolute; left: 96px; top: 230px;
    display: flex; align-items: center; gap: 22px;
  }
  .brand-mark { width: 34px; height: 34px; background: var(--brand-blue); flex: none; }
  .brand-name {
    font-weight: 700; font-size: 58px; line-height: 1.05; color: var(--ink);
  }
  .contact-band {
    position: absolute; left: 0; top: 440px; width: 820px; height: 185px;
    background: var(--brand-blue);
    clip-path: polygon(0 0, 100% 0, 88% 100%, 0 100%);
    color: var(--paper);
  }
  .phone-icon { position: absolute; left: 38px; top: 34px; width: 78px; height: 112px; }
  .phone-number {
    position: absolute; left: 138px; top: 16px;
    font-weight: 800; font-size: 96px; letter-spacing: 2px; line-height: 1;
    white-space: nowrap;
  }
  .website {
    position: absolute; left: 142px; top: 122px;
    font-weight: 700; font-size: 34px; letter-spacing: 1.5px; text-transform: uppercase;
    white-space: nowrap;
  }
  .address-block {
    position: absolute; right: 0; top: 570px; width: 500px; height: 120px;
    background: var(--slate);
    clip-path: polygon(9% 0, 100% 0, 100% 100%, 0 100%);
    color: var(--paper);
  }
  .pin-icon { position: absolute; left: 66px; top: 37px; width: 46px; height: 46px; }
  .address {
    position: absolute; left: 130px; top: 20px;
    font-weight: 500; font-size: 30px; line-height: 1.3; font-style: normal;
    white-space: nowrap;
  }
</style>
</head>
<body>
<main class="sign">
  <div class="facility-photo" role="img" aria-label="Photo of a row of storage units with blue roll-up doors under a blue sky"></div>

  <h1 class="headline">Temperature-Controlled<br>Self Storage Units</h1>

  <div class="brand">
    <span class="brand-mark" aria-hidden="true"></span>
    <p class="brand-name">Brookfell<br>Self Storage</p>
  </div>

  <section class="contact-band">
    <svg class="phone-icon" viewBox="0 0 78 112" aria-hidden="true">
      <rect x="10" y="4" width="58" height="104" rx="9" fill="none" stroke="#fff" stroke-width="7"/>
      <rect x="20" y="18" width="38" height="70" rx="2" fill="#fff"/>
      <circle cx="39" cy="97" r="4" fill="#fff"/>
    </svg>
    <p class="phone-number">478-216-4387</p>
    <p class="website">www.BrookfellStorage.net</p>
  </section>

  <section class="address-block">
    <svg class="pin-icon" viewBox="0 0 46 46" aria-hidden="true">
      <circle cx="23" cy="23" r="21" fill="none" stroke="#fff" stroke-width="2.5"/>
      <path d="M23 34 C17 26 16 23 16 20 a7 7 0 0 1 14 0 c0 3 -1 6 -7 14z" fill="none" stroke="#fff" stroke-width="2.5"/>
      <circle cx="23" cy="20" r="2.5" fill="#fff"/>
    </svg>
    <address class="address">418 Marlow Tenney Pkwy,<br>Centerville, GA 31047</address>
  </section>
</main>
</body>
</html>
```